依頼詳細
PC版のTOPページと下層1ページ(採用情報)のデザイン制作をお願いいたします。
サイトマップ、依頼内容詳細.txtをご確認いただき、動画のテイストを参考にシンプルで見やすいデザインで制作いただきたいです。
スムーズな連絡と軽微な修正にご対応いただける方へご依頼をさせていただきたいです。
ターゲットは木材資材・建築資材・家具建具資材などを必要とする建築会社様、家具・建具製造会社様などです。
ページ数
2ページ
希望イメージ
シンプル 複雑
単色 カラフル
暗い 明るい
日常 高級
遊び心 厳粛
未来的 伝統的
女性的 男性的
希望する色
茶系、緑系、グレー系
納品ファイル
• イラストレーター形式 (.ai)
補足説明
納品ファイルはXDも可です。
添付してあるアニメーションにテイストを合わせ、
木の温かみを感じさせるデザインで制作してください。
コーポレートですが、あまり堅くなり過ぎないようにしたいです。
BtoB向けの会社ではありますが、就職などを考えている若い方が見ても、
面白そうな企業だなという印象も与えたいです。
動画ダウンロードURLを新たに添付いたしましたので
そちらからダウンロードをお願い致します。
■ 選んだ理由

爽やかな緑を使ったデザインが良かったです。

■ 提案者全員のお礼・コメント

たくさんのご提案をいただきありがとうございました。

```html
<!DOCTYPE html>
<html lang="ja">
<head>
<meta charset="utf-8">
<title>KITARIN MORI LUMBER</title>
<link rel="stylesheet" href="https://fonts.googleapis.com/css2?family=Arimo:wght@500;700&family=Josefin+Sans:wght@400;600;700&family=Noto+Sans+JP:wght@400;500;700&display=swap">
<style>
:root{
  --brown:#b0936f;
  --beige:#f4efe8;
  --ink:#222222;
  --dark:#3d3d3d;
  --footer:#4a4a4a;
  --white:#ffffff;
  --tag:#6b6b6b;
}
*{margin:0;padding:0;box-sizing:border-box}
html,body{width:1200px;height:5204px;overflow:hidden;background:var(--white)}
body{position:relative;font-family:"Noto Sans JP",sans-serif;color:var(--ink)}
.abs{position:absolute}

/* header */
.top-bar{left:0;top:0;width:490px;height:80px;background:var(--brown)}
.side-band{left:0;top:0;width:190px;height:660px;background:var(--brown)}
.logo{left:40px;top:26px;font:600 22px "Josefin Sans",sans-serif;color:var(--white);letter-spacing:1px}
.nav{left:680px;top:32px;display:flex;gap:14px;font-size:12px;color:var(--ink);white-space:nowrap}
.btn-contact{left:1020px;top:14px;width:168px;height:50px;background:var(--dark);color:var(--white);font:600 15px "Josefin Sans",sans-serif;letter-spacing:1.5px;display:flex;align-items:center;justify-content:center}
.tree-left{left:180px;top:170px;width:340px;height:490px;background:linear-gradient(180deg,#7fbf4a 0%,#5a9a38 55%,#2b2b2b 100%);border-radius:50% 50% 6px 6px / 40% 40% 6px 6px;opacity:.85}
.tree-right{left:800px;top:80px;width:400px;height:580px;background:linear-gradient(180deg,#6fae44 0%,#4f8d33 60%,#2b2b2b 100%);border-radius:50% 0 6px 6px / 35% 0 6px 6px;opacity:.85}
.hero-title{left:340px;top:405px;font:500 84px "Arimo",sans-serif;line-height:112px;letter-spacing:3px;color:#111;white-space:nowrap}

/* section headings */
.h-en{font:700 46px "Josefin Sans",sans-serif;letter-spacing:8px;color:var(--ink)}
.h-ja{font-size:16px;font-weight:500;margin-top:4px;color:var(--ink)}
.center{left:0;width:1200px;text-align:center}

/* greeting & news */
.greet-bg{left:300px;top:860px;width:900px;height:1160px;background:var(--beige)}
.greet-photo{left:192px;top:952px;width:568px;height:428px;background:radial-gradient(circle at 55% 20%,#f3f7c8 0%,#8fc452 30%,#4f8a2e 70%,#2f5f1c 100%);border-radius:8px;box-shadow:0 6px 18px rgba(0,0,0,.18)}
.greet-card{left:692px;top:1020px;width:400px;height:408px;background:var(--brown);border-radius:8px;padding:52px 28px 0 88px;color:var(--white);font-size:13px;line-height:30px;letter-spacing:1px;overflow:hidden}
.news-list{left:224px;top:1712px;width:896px}
.news-row{display:flex;align-items:center;height:68px;border-bottom:1px solid #bdbdbd;font-size:15px}
.news-date{width:148px}
.news-tag{width:100px;height:26px;background:var(--tag);color:var(--white);font-size:13px;display:flex;align-items:center;justify-content:center;border-radius:4px;margin-right:72px}
.more{width:112px;height:112px;border-radius:50%;background:var(--brown);color:var(--white);font:600 18px "Josefin Sans",sans-serif;letter-spacing:2px;display:flex;align-items:center;justify-content:center}

/* business */
.biz-band{left:0;top:2420px;width:1200px;height:520px;background:var(--beige)}
.slide{border-radius:8px}
.slide-left{left:0;top:2380px;width:176px;height:380px;background:linear-gradient(135deg,#b07a4d,#6d432a);border-radius:0 8px 8px 0}
.slide-main{left:272px;top:2332px;width:656px;height:468px;background:linear-gradient(160deg,#c7ccd3 0%,#8d949c 45%,#b5463f 75%,#6b5a4b 100%)}
.slide-right{left:1020px;top:2380px;width:180px;height:380px;background:linear-gradient(160deg,#5f8a3f,#9b7a55);border-radius:8px 0 0 8px}
.biz-card{left:380px;top:2716px;width:580px;height:130px;background:var(--white);border-radius:6px;padding:22px 28px;font-size:16px;font-weight:500;line-height:27px;letter-spacing:1px}

/* product */
.prod-band{left:0;top:3360px;width:1200px;height:440px;background:var(--beige)}
.prod{width:250px;height:382px;border-radius:8px;box-shadow:0 6px 16px rgba(0,0,0,.2)}
.prod-label{width:250px;text-align:center;font-size:15px;font-weight:500}

/* recruit */
.recruit{left:0;top:4012px;width:1200px;height:348px;background:linear-gradient(90deg,#3a2a1e 0%,#6b4a30 45%,#a77b52 75%,#4a3322 100%);color:var(--white);text-align:center;padding-top:70px}
.recruit .h-en,.recruit .h-ja{color:var(--white)}
.recruit p{font-size:17px;line-height:28px;letter-spacing:1px;margin-top:10px}
.recruit .view{font:600 18px "Josefin Sans",sans-serif;letter-spacing:3px;margin-top:44px}

/* contact */
.contact-box{left:272px;top:4512px;width:656px;height:188px;border:2px solid var(--ink);text-align:center;padding-top:56px}
.contact-box .corner{position:absolute;right:0;bottom:0}

/* footer */
.footer{left:0;top:4848px;width:1200px;height:356px;background:var(--footer);color:var(--white)}
.f-logo{left:112px;top:80px;font:600 28px "Josefin Sans",sans-serif}
.f-info{left:112px;top:160px;font-size:17px;line-height:26px}
.f-nav{left:932px;top:50px;font-size:14px;line-height:38px;list-style:none}
.f-nav li::before{content:"・"}
</style>
</head>
<body>

<header>
  <div class="abs top-bar"></div>
  <div class="abs side-band"></div>
  <div class="abs logo">LOGO</div>
  <nav class="abs nav"><span>会社概要</span><span>事業内容</span><span>取扱商品</span><span>新着情報一覧</span><span>採用情報</span></nav>
  <div class="abs btn-contact">CONTACT US</div>
  <div class="abs tree-left" role="img" aria-label="葉の茂った木のイラスト"></div>
  <div class="abs tree-right" role="img" aria-label="葉の茂った木のイラスト"></div>
  <h1 class="abs hero-title">KITARIN<br>MORI LUMBER</h1>
</header>

<section class="greeting">
  <div class="abs greet-bg"></div>
  <div class="abs" style="left:192px;top:832px"><div class="h-en">GREETING</div><div class="h-ja">ご挨拶</div></div>
  <div class="abs greet-photo" role="img" aria-label="木漏れ日が差す緑の森の写真"></div>
  <div class="abs greet-card">テキストテキストテキストテキストテキストテキストテキストテキストテキストテキストテキストテキストテキストテキストテキストテキストテキストテキストテキストテキストテキストテキストテキストテキストテキストテキストテキストテキストテキストテキストテキストテキスト</div>
</section>

<section class="news">
  <div class="abs" style="left:192px;top:1580px"><div class="h-en">NEWS</div><div class="h-ja">新着情報</div></div>
  <div class="abs news-list">
    <div class="news-row"><span class="news-date">2021.01.01</span><span class="news-tag">カテゴリ</span><span>テキストテキストテキストテキストテキスト</span></div>
    <div class="news-row"><span class="news-date">2021.01.01</span><span class="news-tag">カテゴリ</span><span>テキストテキストテキストテキストテキスト</span></div>
    <div class="news-row"><span class="news-date">2021.01.01</span><span class="news-tag">カテゴリ</span><span>テキストテキストテキストテキストテキスト</span></div>
  </div>
  <div class="abs more" style="left:980px;top:1956px">MORE</div>
</section>

<section class="business">
  <div class="abs center" style="top:2200px"><div class="h-en">BUSINESS</div><div class="h-ja">事業内容</div></div>
  <div class="abs biz-band"></div>
  <div class="abs slide-left" role="img" aria-label="積み重ねた薪の写真"></div>
  <div class="abs slide slide-main" role="img" aria-label="木材加工工場の機械の写真"></div>
  <div class="abs slide-right" role="img" aria-label="森に積まれた丸太の写真"></div>
  <svg class="abs" style="left:212px;top:2540px" width="32" height="48" viewBox="0 0 32 48"><polyline points="24,6 8,24 24,42" fill="none" stroke="#222" stroke-width="4"/></svg>
  <svg class="abs" style="left:956px;top:2540px" width="32" height="48" viewBox="0 0 32 48"><polyline points="8,6 24,24 8,42" fill="none" stroke="#222" stroke-width="4"/></svg>
  <div class="abs biz-card">テキストテキストテキストテキストテキストテキスト<br>テキストテキストテキストテキストテキストテキスト<br>テキストテキストテキストテキスト</div>
</section>

<section class="product">
  <div class="abs center" style="top:3088px"><div class="h-en">PRODUCT</div><div class="h-ja">取扱商品</div></div>
  <div class="abs prod-band"></div>
  <div class="abs prod" style="left:44px;top:3240px;background:linear-gradient(135deg,#e2b98a,#b9804e)" role="img" aria-label="桜材の写真"></div>
  <div class="abs prod-label" style="left:44px;top:3636px">桜材</div>
  <div class="abs prod" style="left:330px;top:3280px;background:linear-gradient(135deg,#e9c9a4,#b88a62)" role="img" aria-label="杉材の写真"></div>
  <div class="abs prod-label" style="left:330px;top:3676px">杉材</div>
  <div class="abs prod" style="left:620px;top:3312px;background:linear-gradient(135deg,#e6c390,#c08d55)" role="img" aria-label="赤松材の写真"></div>
  <div class="abs prod-label" style="left:620px;top:3708px">赤松材</div>
  <div class="abs prod" style="left:904px;top:3360px;background:linear-gradient(135deg,#d9a672,#9c6b3f)" role="img" aria-label="米松材の写真"></div>
  <div class="abs prod-label" style="left:904px;top:3756px">米松材</div>
  <div class="abs more" style="left:184px;top:3752px">MORE</div>
</section>

<section class="abs recruit" role="img" aria-label="木材加工の作業風景の写真">
  <div class="h-en">RECRUIT</div>
  <div class="h-ja">採用情報</div>
  <p>テキストテキストテキストテキストテキストテキストテキスト<br>テキストテキストテキスト</p>
  <div class="view">VIEW　MORE »</div>
</section>

<section class="abs contact-box">
  <div class="h-en">CONTACT US</div>
  <div class="h-ja">お問い合わせ</div>
  <svg class="corner" width="26" height="26" viewBox="0 0 26 26"><polygon points="26,0 26,26 0,26" fill="#222"/></svg>
</section>

<footer class="abs footer">
  <div class="abs f-logo">LOGO</div>
  <div class="abs f-info">〇〇〇〇株式会社<br>〒000-0000<br>〇〇県〇〇市〇〇町2-3-4<br>TEL 000-0000-0000</div>
  <ul class="abs f-nav"><li>会社概要</li><li>事業内容</li><li>取扱商品</li><li>新着情報一覧</li><li>採用情報</li></ul>
</footer>

</body>
</html>
```